Metallic gold accent business card design using new logo

We need a new business card design utilizing our new logo and emphasizing a clean, sophisticated, elegant, easy to read card. Would like to use metallic gold accent, especially with the new logo design, but not overused. Thinking Black with metallic gold printing on reverse side. Front side off white in colour with logo or emblem, and basic information/writing. Logo and emblem should not be too large, would like the overall theme to be classic, even perhaps a bit understated.

Target Market(s)

High end custom home clientele. Sophisticated and elegant

Industry/Entity Type

Residential Construction

Contact Information for Business Card

Looking to use an online provider like ZEP or similar for printing the cards, if you need design details for applying the gold foil, it has to be set up as an element.

Font styles to use
Serif

Colors
fefbee

Requirements
Must have
• My information:
• Walter Brin
• Owner
• walt@ridgelinebuilders.ca
• (902) 555-0173 or (506) 555-0148
• www.ridgelinebuilders.ca
Should not have
• Colourful designs full of images or large logos, large text, flashy gold everywhere

```html
<!DOCTYPE html>
<html lang="en">
<head>
<meta charset="utf-8">
<title>Ridgeline Builders – Business Card</title>
<link rel="stylesheet" href="https://fonts.googleapis.com/css2?family=Cinzel:wght@500;600&family=Open+Sans:wght@400&display=swap">
<style>
  :root {
    --backdrop: #3b3b3b;
    --card-front: #fefbee;
    --card-back: #000000;
    --gold: #cda84e;
    --gold-deep: #a98530;
    --ink: #2b2925;
  }
  * { margin: 0; padding: 0; box-sizing: border-box; }
  html, body { width: 1200px; height: 1000px; overflow: hidden; }
  body { background: var(--backdrop); position: relative; }

  .card {
    position: absolute;
    left: 266px;
    width: 666px;
    height: 397px;
    box-shadow: 0 4px 14px rgba(0,0,0,.45);
  }
  .card--front { top: 74px; background: var(--card-front); }
  .card--back { top: 533px; background: var(--card-back); }

  .brand {
    position: absolute;
    font-family: "Cinzel", serif;
    font-weight: 600;
    text-align: center;
    line-height: 1.15;
  }
  .card--front .brand {
    left: 40px; width: 255px; top: 168px;
    font-size: 26px;
    letter-spacing: 3px;
    color: var(--gold-deep);
  }
  .card--back .brand {
    left: 0; width: 100%; top: 162px;
    font-size: 40px;
    letter-spacing: 5px;
    color: var(--gold);
  }

  .divider {
    position: absolute;
    left: 319px; top: 109px;
    width: 1px; height: 178px;
    background: var(--gold-deep);
  }

  .contact {
    position: absolute;
    left: 354px; top: 107px;
  }
  .contact__name {
    font-family: "Cinzel", serif;
    font-weight: 600;
    font-size: 19px;
    letter-spacing: .5px;
    color: var(--gold-deep);
  }
  .contact__role {
    font-family: "Open Sans", sans-serif;
    font-size: 15px;
    color: var(--ink);
    margin-top: 1px;
  }
  .contact__list {
    list-style: none;
    margin-top: 39px;
  }
  .contact__item {
    display: flex;
    align-items: center;
    gap: 7px;
    font-family: "Open Sans", sans-serif;
    font-size: 16px;
    color: var(--ink);
    height: 24px;
  }
  .contact__icon { width: 14px; height: 14px; flex: none; fill: var(--gold-deep); }
  .contact__icon--line { fill: none; stroke: var(--gold-deep); }

  .back__url {
    position: absolute;
    left: 0; width: 100%; top: 347px;
    text-align: center;
    font-family: "Open Sans", sans-serif;
    font-size: 16px;
    color: var(--gold);
  }
</style>
</head>
<body>
  <section class="card card--front">
    <div class="brand">RIDGELINE<br>BUILDERS</div>
    <div class="divider"></div>
    <div class="contact">
      <div class="contact__name">WALTER BRIN</div>
      <div class="contact__role">Owner</div>
      <ul class="contact__list">
        <li class="contact__item">
          <svg class="contact__icon" viewBox="0 0 14 14" aria-hidden="true"><path d="M1 4c0-2 2-3 6-3s6 1 6 3v1h-3V4H4v1H1z"/><path d="M3 6h8l2 6H1z"/></svg>
          (506) 555-0148
        </li>
        <li class="contact__item">
          <svg class="contact__icon" viewBox="0 0 14 14" aria-hidden="true"><path d="M1 4c0-2 2-3 6-3s6 1 6 3v1h-3V4H4v1H1z"/><path d="M3 6h8l2 6H1z"/></svg>
          (902) 555-0173
        </li>
        <li class="contact__item">
          <svg class="contact__icon contact__icon--line" viewBox="0 0 14 14" aria-hidden="true"><path d="M1 3h12v8H1z M1 3l6 5 6-5" stroke-width="1.4"/></svg>
          walt@ridgelinebuilders.ca
        </li>
        <li class="contact__item">
          <svg class="contact__icon contact__icon--line" viewBox="0 0 14 14" aria-hidden="true"><circle cx="7" cy="7" r="5.5" stroke-width="1.4"/><path d="M1.5 7h11M7 1.5c-3 3-3 8 0 11M7 1.5c3 3 3 8 0 11" stroke-width="1"/></svg>
          www.ridgelinebuilders.ca
        </li>
      </ul>
    </div>
  </section>

  <section class="card card--back">
    <div class="brand">RIDGELINE<br>BUILDERS</div>
    <div class="back__url">www.ridgelinebuilders.ca</div>
  </section>
</body>
</html>
```